Packaging design Project - for lovers of the distant lands of the Andes and it's organic culture

Oyé Oyé, friends of the organic terroir! Lovers of the distant lands and the Andes, this mission is for you!
Our baby, Verdant Ridge, is preparing for birth! This is your chance to make us dream.
Our values: Giving life to the Authentic Terroir of Bolivia. For it ; provide sustainable solutions for the local terroir of our organic crops.

What is the terroir? (french word). It’s that connection to Human and Earth. Humanity is respect for culture, ancestral know-how, artisanal work. The Earth is the environment, the ecology, this is what the Indians called the Pachamama.

At an altitude of 4200m, La Quinoa de Verdant Ridge is not cultivated in the plains with combine harvesters. It is cultivated by hand on the feet and on the mountainside. The fallow (66% of the land) allows the soil and the Gods of the Andean cosmovision to come to life.
Our mission is to bring these values to life through these products that we import; White Quinoa , red, Duo (red and white) and Trio (red, black and white).
For this, we are looking for a packaging design. You bring creativity and together we validate the content !

The finished product is intended for end consumers (specialized organic store for example). Its format is 18cm high x 8.5cm long and 4.5cm wide. We therefore need a graphic charter for the entire packaging; or 4 sides totaling 26 cm for 18 cm high. You will mainly work on the visual of the main page (18x8.5), illustration of our committed values through the colors of Bolivia: Red, Yellow and Green. The country being very colorful by nature (google search: "Aguayo cloth") we want to create a breath of life through the liveliness of the colors, that the products are obvious, just like these famous Bolivian Aguayo.
Our Quinoa comes from an authentic terroir. It is harvested by hand and is very rich in nutrition.
We had already worked on packaging, which we want to improve and make more alive. It’s true that the black print kraft background isn’t the best.
Here are some snippets of text taken from this first packaging:
"While the Quinoa of the plains depletes the soils of the Bolivian altiplano ..."
"The Verdant Ridge Quinoa comes from areas that are difficult to access, at the foot and on the mountainside where the cultivation is done by hand and with respect for ancestral traditions"
Mountain Quinoa committed!
Provides a local solution for the Bolivian terroir.
By respecting the Earth: the Pachamama with the fallow of 66% of the land. A return to the sources, as in the time of the Incas, letting the llamas make the biodiversity of the high plains flourish.
By respect for the Human Being and for future generations. Cultivated and distributed preserving the essence of Andean culture, the rights and croyances of Quechua producers and honoring the values of the Bolivian people.

In summary, I invite you to discover the energy of the project through this video: https://www.clipvista-example.net/watch?v=Kp3TrwQ9zLe
And these few images (attachments)…
And our logo of course on the PDF of our project presentation!

Note: Ideally, the design could include a visual of the raw Quinoa so client could see the product on the packaging. (as enclosed pictures!!!)

And most of all... have fun! Let your creativity EXPLODE! That's exactly what we want you to do. Just plenty be yourself... that's how our client will say 'Whaow!' looking at your art!

enjoy!

Target Market(s)

Premium Quinoa consumers. - Engaged consumers for causes and belief throught their product consumption

Font styles to use
Other font styles liked:
• earth quest (for head lines)

Colors
acd136
9bcb3c
ec1f27
f04a50
f78f20
f37122
ffc214
fece3e
fbed22

Requirements
Must have
• Colors (red, green and yellow)
Mountain as backgroud (enclosed)
Quinoa field on the feet or aside the mountain
Autoctones (people)
Quinoa grains (as it is raw)
Nice to have
• Detail of expressing Quinoa is handly cultivated (hand harvest)
Tipical houses in the back
Aguayo motifs (for the graphic charter maybe?)

```html
<!DOCTYPE html>
<html lang="fr">
<head>
<meta charset="utf-8">
<title>Verdant Ridge – Quinoa label</title>
<link href="https://fonts.googleapis.com/css2?family=Bebas+Neue&family=Montserrat:wght@300;400;700&display=swap" rel="stylesheet">
<style>
  :root {
    --backdrop: #efe9df;
    --red: #dc2a2a;
    --orange: #e8702a;
    --amber: #f1a022;
    --yellow: #f4bb1c;
    --olive: #a6a537;
    --green: #2f8c43;
    --deep-green: #128443;
    --ink: #ffffff;
    --grain-light: #e3cfa6;
    --grain-dark: #a8875a;
  }
  * { margin: 0; padding: 0; box-sizing: border-box; }
  html, body {
    width: 1200px;
    height: 1133px;
    overflow: hidden;
    background: var(--backdrop);
  }
  .canvas {
    position: relative;
    width: 1200px;
    height: 1133px;
  }
  .label {
    position: absolute;
    left: 351px;
    top: 40px;
    width: 497px;
    height: 1053px;
    overflow: hidden;
    color: var(--ink);
    background: linear-gradient(180deg,
      var(--red) 0%,
      var(--orange) 22%,
      var(--amber) 40%,
      var(--yellow) 52%,
      var(--olive) 70%,
      var(--green) 88%,
      var(--deep-green) 100%);
    box-shadow: 0 0 24px rgba(255, 240, 200, 0.7);
  }
  .product-title {
    position: absolute;
    left: 28px;
    top: 70px;
    width: 440px;
    font-family: "Bebas Neue", "Arial Narrow", sans-serif;
    font-size: 198px;
    line-height: 1;
    letter-spacing: 2px;
    text-align: center;
  }
  .origin {
    position: absolute;
    left: 33px;
    top: 239px;
    width: 430px;
    font-family: "Montserrat", Arial, sans-serif;
    font-weight: 700;
    font-size: 21.5px;
    letter-spacing: 0.2px;
    text-align: center;
    white-space: nowrap;
  }
  .brand {
    position: absolute;
    left: 30px;
    top: 300px;
    width: 380px;
    height: 330px;
    display: flex;
    flex-direction: column;
    align-items: center;
    justify-content: center;
    gap: 14px;
  }
  .brand-mark {
    width: 150px;
    height: 150px;
    border-radius: 50%;
    background: var(--ink);
  }
  .brand-name {
    font-family: "Montserrat", Arial, sans-serif;
    font-weight: 700;
    font-size: 40px;
    line-height: 1;
  }
  .brand-tagline {
    font-family: "Montserrat", Arial, sans-serif;
    font-weight: 700;
    font-size: 22px;
    line-height: 1;
  }
  .claim {
    position: absolute;
    left: 33px;
    top: 664px;
    font-family: "Montserrat", Arial, sans-serif;
    font-weight: 400;
    font-size: 19.5px;
    letter-spacing: 0.2px;
    white-space: nowrap;
  }
  .features {
    position: absolute;
    left: 31px;
    top: 718px;
    display: flex;
    gap: 30px;
    list-style: none;
  }
  .feature {
    display: flex;
    align-items: center;
    gap: 14px;
    font-family: "Montserrat", Arial, sans-serif;
    font-weight: 400;
    font-size: 16.5px;
    line-height: 1.45;
  }
  .feature-icon {
    width: 48px;
    height: 48px;
    flex: none;
  }
  .product-photo {
    position: absolute;
    left: 0;
    top: 800px;
    width: 480px;
    height: 253px;
    background: radial-gradient(ellipse 70% 80% at 40% 65%,
      var(--grain-light) 0%, #d6bd8f 55%, var(--grain-dark) 85%, rgba(168,135,90,0) 100%);
  }
</style>
</head>
<body>
<main class="canvas">
  <section class="label">
    <h1 class="product-title">QUINOA</h1>
    <p class="origin">DE MONTAGNES DE BOLIVIE</p>

    <div class="brand">
      <div class="brand-mark" role="img" aria-label="Illustration area: Andean farmer and mountain peaks under stars"></div>
      <p class="brand-name">Verdant Ridge</p>
      <p class="brand-tagline">Terroir Authentique</p>
    </div>

    <p class="claim">A HAUTE VALEUR NUTRITIVE</p>

    <ul class="features">
      <li class="feature">
        <svg class="feature-icon" viewBox="0 0 48 48" fill="none" stroke="currentColor" stroke-width="1.8" stroke-linecap="round" stroke-linejoin="round" aria-hidden="true">
          <circle cx="24" cy="24" r="22"/>
          <path d="M24 28 V17"/>
          <path d="M24 21 C19 21 17 18 17 15 C21 15 24 17 24 21"/>
          <path d="M24 19 C28 19 31 16 31 13 C27 13 24 15 24 19"/>
          <path d="M12 30 H18 L24 33 H30 C32 33 32 30 30 30 H25"/>
          <path d="M12 35 H20 L27 37 L36 31"/>
        </svg>
        <span>Harvest<br>by Hand</span>
      </li>
      <li class="feature">
        <svg class="feature-icon" viewBox="0 0 48 48" fill="none" stroke="currentColor" stroke-width="1.8" stroke-linecap="round" stroke-linejoin="round" aria-hidden="true">
          <circle cx="24" cy="24" r="22"/>
          <path d="M10 32 L20 16 L26 25 L30 20 L38 32 Z"/>
          <path d="M17 21 L20 23 L23 20"/>
        </svg>
        <span>From The<br>Mountains</span>
      </li>
    </ul>

    <div class="product-photo" role="img" aria-label="Photo of raw quinoa grains heaped with a wooden scoop"></div>
  </section>
</main>
</body>
</html>
```